Patient Fact sheets for medical conditions and treatments

Hi,

I need a new design for my patient fact sheets. I am moving from my current clinic and I am looking from a new look.

I have attached
1. a current Fact sheet
2. New home page to the website
3. New Logo.

They need to be single page and easily readable for patients.

The will be in both PDF and print form in the future.

Target Market(s)

Patients with chronic pain age 40+

Font styles to use
Serif

Requirements
Must have
• My logo, should be inline with design elements on the Front page provided.

Please use the same font as the Logo

```html
<!DOCTYPE html>
<html lang="en">
<head>
<meta charset="utf-8">
<title>Fact Sheet – Platelet Rich Plasma (PRP) Therapy</title>
<link rel="stylesheet" href="https://fonts.googleapis.com/css2?family=Cinzel:wght@400;500;700&family=Baskervville&display=swap">
<style>
  :root {
    --navy: #1f1f55;
    --ink: #2e2e2e;
    --panel: #e7e7e7;
    --footer: #2a2a2a;
    --footer-ink: #e9e9e9;
    --footer-muted: #c9c9c9;
    --rule: #6a6a6a;
  }
  * { box-sizing: border-box; margin: 0; padding: 0; }
  html, body { width: 848px; height: 1200px; overflow: hidden; background: #fff; }
  body { font-family: "Baskervville", Georgia, serif; color: var(--ink); }
  .sheet { position: relative; width: 848px; height: 1200px; overflow: hidden; }

  .side-panel { position: absolute; left: 555px; top: 0; width: 293px; height: 977px; background: var(--panel); }
  .hero-photo {
    position: absolute; left: 555px; top: 0; width: 293px; height: 267px;
    background: linear-gradient(120deg, #c9c9c9 0%, #ececec 40%, #f7f5ee 65%, #e6dfb8 100%);
  }
  .clinician-name {
    position: absolute; left: 612px; top: 58px;
    display: flex; align-items: center; gap: 8px;
    font-family: "Baskervville", Georgia, serif; font-weight: 400;
    font-size: 19px; line-height: 22px; color: var(--navy);
  }
  .clinician-name .mark { width: 9px; height: 9px; background: var(--navy); }

  .eyebrow {
    position: absolute; left: 41px; top: 56px;
    font-family: "Cinzel", serif; font-weight: 400; font-size: 27px; color: var(--navy); letter-spacing: 0.5px;
  }
  .title {
    position: absolute; left: 41px; top: 102px; width: 500px;
    font-family: "Cinzel", serif; font-weight: 700; font-size: 37px; line-height: 46px;
    color: var(--navy); letter-spacing: 0.5px;
  }

  .column { position: absolute; font-size: 13.6px; line-height: 18.5px; }
  .col-one { left: 41px; top: 232px; width: 228px; }
  .col-two { left: 293px; top: 232px; width: 228px; }
  .col-three { left: 584px; top: 294px; width: 232px; }

  .section-heading {
    font-family: "Cinzel", serif; font-weight: 500; font-size: 15.5px; line-height: 21px;
    color: var(--navy); letter-spacing: 0.2px; margin-bottom: 7px;
  }
  .column p { margin-bottom: 7px; }
  .column section + section { margin-top: 20px; }

  .bullets { list-style: none; }
  .bullets li { position: relative; padding-left: 18px; margin-bottom: 4px; line-height: 17px; }
  .bullets li::before {
    content: ""; position: absolute; left: 1px; top: 7px; width: 4px; height: 4px;
    border-radius: 50%; background: var(--ink);
  }
  .plain-list { margin-bottom: 6px; }
  .plain-list li { margin-bottom: 3.5px; line-height: 18.4px; }

  .footer { position: absolute; left: 0; top: 977px; width: 848px; height: 223px; background: var(--footer); color: var(--footer-ink); }
  .footer-heading {
    position: absolute; left: 41px; top: 32px;
    font-family: "Cinzel", serif; font-weight: 400; font-size: 18.5px; letter-spacing: 1px; color: #fff;
  }
  .contact { position: absolute; left: 41px; top: 62px; font-size: 13.2px; line-height: 17px; }
  .contact .org { font-weight: 700; color: #fff; }
  .contact .phone { margin-top: 4px; }
  .website { position: absolute; left: 255px; top: 177px; font-size: 13.2px; }
  .footer-rule { position: absolute; left: 424px; top: 27px; width: 1px; height: 162px; background: var(--rule); }
  .disclaimer { position: absolute; left: 455px; top: 34px; width: 355px; color: var(--footer-muted); }
  .disclaimer h3 { font-family: "Baskervville", serif; font-weight: 400; font-size: 11.5px; letter-spacing: 0.8px; margin-bottom: 11px; }
  .disclaimer p { font-size: 10.4px; line-height: 14.2px; }
</style>
</head>
<body>
<div class="sheet">
  <div class="side-panel"></div>
  <div class="hero-photo" role="img" aria-label="Photo of gloved hand holding test tubes of separated platelet rich plasma"></div>
  <div class="clinician-name"><span class="mark"></span>Dr Lena Marsh</div>

  <div class="eyebrow">FACT SHEET</div>
  <h1 class="title">Platelet Rich Plasma (PRP) Therapy</h1>

  <div class="column col-one">
    <section>
      <h2 class="section-heading">WHAT IS PRP?</h2>
      <p>Platelet-Rich Plasma (PRP) is concentrated platelets and white blood cells derived from your own blood.</p>
      <p>Platelet Rich Plasma Injection Therapy (PRP therapy), is a growing treatment approach for soft tissue injuries including tendon, muscle and ligaments. It is also showing good results for mild to moderate osteoarthritis.</p>
      <p>While this approach has been used overseas for many years, it’s fairly new to Australia in the treatment of musculoskeletal and orthopaedic conditions.</p>
    </section>
    <section>
      <h2 class="section-heading">HOW DOES PRP WORK?</h2>
      <p>Some tissues in the body have a poor blood supply or respond poorly to excessive load, ultimately failing to heal naturally. While some of our primary treatment such as physiotherapy, massage, biomechanical correction and other forms of treatment are used to treat these soft tissue injuries, sometimes the body fails to respond.</p>
      <p>PRP therapy utilises the healing properties in blood to allow a healing reaction to occur in a tissue that’s not healing on its own. Our blood has small granules called ‘platelets’, which contain special growth factors that</p>
    </section>
  </div>

  <div class="column col-two">
    <section>
      <p>when released, allow stem cells in the particular tissue to ‘switch’ on and cause new tissue to be created and heal the injured area.</p>
      <p>Take the example of achilles tendinopathy. If the achilles is painful, thickened and not responding to rehabilitation, then the sports physician will inject the PRP into the achilles which will cause the tendon cells (tenocytes/fibroblasts) to create new achilles collagen to strengthen the achilles. White blood cells also enter the area to mop up any achilles tissue that may have been damaged due to the ongoing pain and thickening in the area.</p>
    </section>
    <section>
      <h2 class="section-heading">ROLE OF PLATELETS &amp;<br>GROWTH FACTORS</h2>
      <p>PRP contains highly concentrated platelets. Platelets have been identified to secrete growth factors, which are known to play a role in:</p>
      <ul class="bullets">
        <li>increasing tissue vascularity and increasing the rate of epithelial tissue production (wound healing)</li>
        <li>attracting other cells that fight infection</li>
        <li>acting as a seal during closures</li>
        <li>providing an immediate surgical hemostatic agent (reduction of bleeding)</li>
        <li>osteogenesis (bone regeneration and repair).</li>
      </ul>
    </section>
  </div>

  <div class="column col-three">
    <section>
      <h2 class="section-heading">WHAT CAN PRP TREAT?</h2>
      <p>PRP therapy can be used for:</p>
      <ul class="bullets plain-list">
        <li>orthopedic surgery</li>
        <li>cardiac surgery</li>
        <li>plastic and cosmetic surgery</li>
        <li>ear, nose, throat (ENT) surgery</li>
        <li>oral maxillofacial surgery</li>
        <li>neurosurgery</li>
        <li>vascular surgery</li>
        <li>wound healing</li>
        <li>burn care.</li>
      </ul>
      <p>Ask your doctor whether platelet-rich plasma is appropriate for your surgical procedure</p>
    </section>
    <section>
      <h2 class="section-heading">WHAT ARE THE EXPECTED<br>RESULTS OF PRP?</h2>
      <p>Because the goal of PRP therapy is to resolve pain through healing, it could prove to have lasting results. Initial improvement may be seen within a few weeks, gradually increasing as the healing progresses. Research studies and clinical practice have shown PRP therapy to be very effective at relieving pain and returning patients to their normal lives. The need for surgery can also be greatly reduced by treating injured tissues before the damage progresses and the condition is irreversible.</p>
    </section>
  </div>

  <footer class="footer">
    <div class="footer-heading">FOR MORE INFORMATION</div>
    <div class="contact">
      <div class="org">Harbour Pain Clinic</div>
      <div>Linden House, Ground Floor<br>48 Arden Street<br>Northvale VIC 3199</div>
      <div class="phone">T&nbsp; 03 9000 4120<br>F&nbsp; 03 9000 4121<br>E&nbsp; info@harbourpain.com.au</div>
    </div>
    <div class="website">harbourpain.com.au</div>
    <div class="footer-rule"></div>
    <div class="disclaimer">
      <h3>DISCLAIMER</h3>
      <p>Please note the contents contained in this Patient Fact Sheet are not intended as a substitute for your own independent health professional’s advice, diagnosis or treatment. At Harbour Pain Clinic, we assess every patient’s condition individually. As leaders in pain intervention, we aim to provide advanced, innovative, and evidence-based treatments tailored to suit each patient. As such, recommended treatments and their outcomes will vary from patient to patient. If you would like to find out whether our treatments are suitable for your specific condition, please speak to one of our doctors at the time of your consultation.</p>
    </div>
  </footer>
</div>
</body>
</html>
```